Social responsible Renewable Energy company

We at voltaQ are an independent power producer company founded in 2021 that handles large scale deployment of Renewable Energy and carbon neutral Energy as a service model. We offer turnkey solutions using solar panel systems and this could be incorporated in our business cards. You can also find our logo in the documents provided. Another key issue is that the business cards will be printed on recicled paper, not sure if this is a limitation in deciding the design. The recycled sign should also be added on the business card and stating that the paper used was recycled. Our website is www.myvoltaq.example. It should also be very professional, not too dreamy but still needs to capture your imagination. We are really excited to get your ideas !

Target Market(s)

Renewable Energy market

Contact Information for Business Card

The business card will be printed on recycled paper. Name of the company is voltaQ. Website is www.myvoltaq.example

Requirements
Nice to have
• Our motto: Clean Energy As A Service, Built Together.

```html
<!DOCTYPE html>
<html lang="en">
<head>
<meta charset="utf-8">
<title>voltaQ Business Card</title>
<link href="https://fonts.googleapis.com/css2?family=Open+Sans:wght@400;600;700;800&display=swap" rel="stylesheet">
<style>
  :root {
    --bg: #d6d6d4;
    --card: #fbfbfb;
    --navy: #2a5683;
    --blue: #2f8ee0;
    --ink: #2b2b2b;
    --faint: #e6ebf0;
    --eco-green: #2f6b3a;
  }
  * { margin: 0; padding: 0; box-sizing: border-box; }
  html, body { width: 1200px; height: 675px; overflow: hidden; }
  body {
    background: var(--bg);
    font-family: "Open Sans", Arial, sans-serif;
    position: relative;
  }
  .card {
    position: absolute;
    width: 504px;
    height: 288px;
    background: var(--card);
    border-radius: 14px;
    box-shadow: 0 10px 26px rgba(0,0,0,0.18);
    overflow: hidden;
  }
  .card-front { left: 66px; top: 194px; }
  .card-back  { left: 630px; top: 194px; }

  .faint-disc {
    position: absolute;
    border-radius: 50%;
    background: var(--faint);
  }
  .card-front .faint-disc { width: 250px; height: 250px; left: 8px; top: 4px; }
  .card-back .faint-disc  { width: 280px; height: 280px; left: 70px; top: 4px; }

  .wordmark {
    position: absolute;
    font-weight: 800;
    color: var(--navy);
    letter-spacing: -1px;
    line-height: 1;
  }
  .tagline {
    position: absolute;
    font-weight: 600;
    color: var(--ink);
    white-space: nowrap;
    line-height: 1.2;
  }
  .card-front .wordmark { font-size: 72px; left: 108px; top: 36px; }
  .card-front .tagline  { left: 112px; top: 114px; font-size: 12.5px; }

  .divider {
    position: absolute;
    left: 24px; right: 40px; top: 172px;
    height: 1.5px;
    background: var(--blue);
  }
  .contact {
    position: absolute;
    list-style: none;
    font-size: 12.5px;
    color: var(--ink);
  }
  .contact li { display: flex; align-items: center; gap: 8px; height: 20px; white-space: nowrap; }
  .contact svg { width: 13px; height: 13px; flex: none; }
  .contact-left  { left: 24px; top: 182px; }
  .contact-right { left: 250px; top: 214px; }

  .person { position: absolute; right: 44px; top: 136px; text-align: right; }
  .person-name { font-size: 20px; font-weight: 800; color: var(--blue); letter-spacing: 1px; line-height: 1; }
  .person-role { font-size: 10.5px; font-weight: 700; color: var(--ink); line-height: 1.3; }

  .card-back .wordmark { font-size: 86px; left: 118px; top: 92px; }
  .card-back .tagline  { left: 124px; top: 184px; font-size: 13.5px; }

  .badge-recycled { position: absolute; left: 22px; top: 22px; width: 34px; height: 34px; border-radius: 50%; border: 2.5px solid var(--eco-green); }
  .badge-cert { position: absolute; right: 22px; bottom: 22px; width: 34px; height: 34px; border: 2.5px solid var(--eco-green); }
</style>
</head>
<body>
  <section class="card card-front" aria-label="Business card front">
    <div class="faint-disc"></div>
    <div class="wordmark">voltaQ</div>
    <div class="tagline">Clean Energy As A Service, Built Together</div>

    <div class="person">
      <div class="person-name">NAME</div>
      <div class="person-role">Designation</div>
    </div>

    <div class="divider"></div>

    <ul class="contact contact-left">
      <li>
        <svg viewBox="0 0 14 14"><rect width="14" height="14" rx="2" fill="#2f8ee0"/><path d="M7 2.5a3 3 0 0 0-3 3c0 2.2 3 5.5 3 5.5s3-3.3 3-5.5a3 3 0 0 0-3-3z" fill="#fff"/><circle cx="7" cy="5.5" r="1" fill="#2f8ee0"/></svg>
        Address Line, City, Zip code
      </li>
      <li>
        <svg viewBox="0 0 14 14"><rect width="14" height="14" rx="2" fill="#2f8ee0"/><path d="M4 3.5l2 .3.6 2-1.1.8a5 5 0 0 0 2.9 2.9l.8-1.1 2 .6.3 2c-4.5.5-8-3-7.5-7.5z" fill="#fff"/></svg>
        Contact Number
      </li>
    </ul>

    <ul class="contact contact-right">
      <li>
        <svg viewBox="0 0 14 14"><rect width="14" height="14" rx="2" fill="#2f8ee0"/><rect x="3" y="4" width="8" height="6" fill="none" stroke="#fff" stroke-width="1.2"/><path d="M3 4l4 3.2L11 4" fill="none" stroke="#fff" stroke-width="1.2"/></svg>
        hello@myvoltaq.example
      </li>
      <li>
        <svg viewBox="0 0 14 14"><rect width="14" height="14" rx="2" fill="#2f8ee0"/><circle cx="7" cy="7" r="4" fill="none" stroke="#fff" stroke-width="1.1"/><path d="M3 7h8M7 3c-2 2.5-2 5.5 0 8M7 3c2 2.5 2 5.5 0 8" fill="none" stroke="#fff" stroke-width="1"/></svg>
        www.myvoltaq.example
      </li>
    </ul>
  </section>

  <section class="card card-back" aria-label="Business card back">
    <div class="faint-disc"></div>
    <div class="badge-recycled" role="img" aria-label="Recycled paper badge"></div>
    <div class="wordmark">voltaQ</div>
    <div class="tagline">Clean Energy As A Service, Built Together</div>
    <div class="badge-cert" role="img" aria-label="Paper certification badge"></div>
  </section>
</body>
</html>
```